Varga Lillas Physiotherapy Business Card Vienna

We need a business card design for a newly created Physiotherapy company based in Vienna Austria.
We seek a simple, modern, minimalist design without too much color variation. The font should look young/fresh, but definitely not childish or so. Since we are a starting Business, we currently haven't got a logo, if you feel like a logo would fit your design, feel free to use one, but it's not necessary.
Target Market(s)
Healthcare, young and elderly people with mobility issues
Industry/Entity Type
Health And Wellness
Contact Information for Business Card
Name: Lilla Varga
Title description: Physiotherapist
Phone num: +43 664 5290 4816
e-mail: lilla.praxis@brelomail.com
Colors
Designer to choose colors to be used in the design.
Requirements
Must have
- Final design language must be in German, basically, the Title Description needs to be "Physiotherapeutin" the other details remain as in the English Language.
Nice to have
- Simple, modern, minimalist design
Should not have
- too many colors, Obvious use of a skeleton, skull, spline

```html
<!DOCTYPE html>
<html lang="de">
<head>
<meta charset="utf-8">
<title>Lilla Varga – Physiotherapeutin</title>
<link href="https://fonts.googleapis.com/css2?family=Montserrat:wght@700&family=Jost:wght@300&display=swap" rel="stylesheet">
<style>
  :root {
    --backdrop: #2c3f44;
    --card-dark: #323232;
    --card-pattern: #2d2d2d;
    --card-light: #ffffff;
    --ink-light: #ffffff;
    --ink-dark: #222222;
  }
  html, body {
    margin: 0;
    padding: 0;
    width: 1200px;
    height: 1000px;
    overflow: hidden;
    background: var(--backdrop);
  }
  .canvas {
    position: relative;
    width: 1200px;
    height: 1000px;
  }
  .card {
    position: absolute;
    left: 337px;
    top: 237px;
    width: 526px;
    height: 527px;
    background: var(--card-light);
    overflow: hidden;
  }
  .card__panel {
    position: absolute;
    left: 196px;
    top: 0;
    width: 330px;
    height: 527px;
    background: linear-gradient(135deg, var(--card-dark), var(--card-pattern));
  }
  .card__name {
    position: absolute;
    left: 184px;
    margin: 0;
    font-family: "Montserrat", sans-serif;
    font-weight: 700;
    color: var(--ink-light);
    letter-spacing: 5px;
    line-height: 1;
    white-space: nowrap;
  }
  .card__name--first { top: 127px; }
  .card__name--last { top: 242px; }
  .card__name .initial { font-size: 98px; }
  .card__name .rest { font-size: 72px; }
  .card__title-band {
    position: absolute;
    left: 0;
    top: 352px;
    width: 526px;
    height: 70px;
    background: var(--card-light);
  }
  .card__title {
    position: absolute;
    left: 4px;
    top: 13px;
    margin: 0;
    font-family: "Jost", sans-serif;
    font-weight: 300;
    font-size: 31px;
    letter-spacing: 13.4px;
    color: var(--ink-dark);
    white-space: nowrap;
  }
  .card__contact {
    position: absolute;
    right: 37px;
    top: 440px;
    text-align: right;
    font-family: "Jost", sans-serif;
    font-weight: 300;
    color: var(--ink-light);
  }
  .card__phone {
    display: block;
    font-size: 25px;
    letter-spacing: 0.5px;
    line-height: 36px;
  }
  .card__email {
    display: block;
    font-size: 18.5px;
    line-height: 30px;
  }
</style>
</head>
<body>
<div class="canvas">
  <div class="card">
    <div class="card__panel" role="img" aria-label="Dunkle Fläche mit feinem Rautenmuster"></div>
    <h1 class="card__name card__name--first"><span class="initial">L</span><span class="rest">ILLA</span></h1>
    <h1 class="card__name card__name--last"><span class="initial">V</span><span class="rest">ARGA</span></h1>
    <div class="card__title-band">
      <p class="card__title">physiotherapeutin</p>
    </div>
    <div class="card__contact">
      <span class="card__phone">+43 664 5290 4816</span>
      <span class="card__email">lilla.praxis@brelomail.com</span>
    </div>
  </div>
</div>
</body>
</html>
```